Marrowby Cove Soda

We need an eco-label designed to go on our soda bottles that will be for sale on a tiny island off the east coast of Australia. The label is a printed card (double sided) that is 60mm wide and 180mm long. There is a 40mm by 40mm hole that is used to place on the bottle, as shown in the photos. One side is the back label, this has some regulatory requirements such as a panel of % of dietary intake, an ingredient list and a line that reads "Batch:_________". That is standard on each back panel. The front needs to have the name of the soda flavour and design of label. The reverse will need to have a blurb about us, our story and how to recycle the bottle.

We would like the design to be funny, possibly using Captain Sir Bertram Quill's photoshopped image (he is a grizzly dude the island is named after see pixora search) or anything you talented people come up with.

We want to use the same format and then will need to change the name for the flavours, change the ingredients list and replace the standard box for the % daily intake.

Target Market(s)

The Product will stand next to the big soda companies that all know and thus must stand out visually from them to get the customer to have a second look at the product

Industry/Entity Type

Soda

Requirements
Must have
• Space for the Flavour on the front ie "Lemonade". "Batch:_________" at the base of the back panel.
Nice to have
• Island feel, Possibly using "Captain Sir Quill" holding a drink?!? Palms, sunsets

```html
<!DOCTYPE html>
<html lang="en">
<head>
<meta charset="utf-8">
<title>Marrowby Cove Soda – Bottle Label</title>
<link rel="stylesheet" href="https://fonts.googleapis.com/css2?family=Great+Vibes&family=Poiret+One&display=swap">
<style>
  :root {
    --paper: #ffffff;
    --frame: #222222;
    --sand: #e9d4b4;
    --sand-gold: #e8c37a;
    --sea: #3fb3d6;
    --sea-deep: #1b8fc0;
    --sky: #5cbcf0;
    --sky-pale: #bfe6fb;
    --sky-deep: #0a3ad6;
    --ink: #111111;
    --teal: #1a8db0;
    --brand-blue: #1da2e8;
    --ring: #6f9cf2;
    --panel-pale: #b9dcfb;
    --hole: #ffffff;
    --script: "Great Vibes", cursive;
    --thin: "Poiret One", sans-serif;
  }
  * { box-sizing: border-box; margin: 0; padding: 0; }
  html, body { width: 1200px; height: 847px; overflow: hidden; background: var(--paper); }
  .sheet {
    position: relative; width: 1200px; height: 847px;
    border: 1px solid var(--frame); background: var(--paper);
  }
  .label {
    position: absolute; top: 58px; width: 243px; height: 731px;
    overflow: hidden; border: 1px solid #c9b08a;
  }
  .label--back { left: 237px; }
  .label--reverse { left: 675px; }
  .scenery { position: absolute; inset: 0; }
  .label--back .scenery {
    background: linear-gradient(to bottom,
      var(--sand) 0px, #e3d4c2 70px, #d9ecf2 88px, var(--sea) 100px,
      #9fd6f0 150px, #dff3fc 215px, #a8dcf6 270px, var(--sky) 330px,
      #6cc2f0 520px, var(--sky) 600px, var(--sea-deep) 625px,
      var(--sea) 655px, #cfe6e3 668px, var(--sand) 680px, var(--sand) 731px);
  }
  .label--reverse .scenery {
    background: linear-gradient(to bottom,
      var(--sand-gold) 0px, #f0d497 95px, #4fd0e0 105px, #1aa7cf 130px,
      #8fd2f6 140px, var(--sky-pale) 175px, #5aaef2 220px, #2f7ee8 300px,
      var(--sky-deep) 360px, #1560e4 470px, #59b0f0 530px, var(--sky-pale) 585px,
      #5dc3e8 615px, #27a8d2 630px, #f3d79a 645px, var(--sand-gold) 731px);
  }
  .hole {
    position: absolute; top: 284px; left: 40px; width: 162px; height: 162px;
    background: var(--hole); border: 1px solid #333;
  }
  .flipped { position: absolute; transform: rotate(180deg); }
  .flavour {
    left: 8px; top: 12px; width: 120px;
    font-family: var(--script); font-size: 32px; color: var(--teal); line-height: 1;
  }
  .brand { left: 53px; top: 96px; width: 140px; height: 140px; }
  .brand svg { position: absolute; inset: 0; }
  .brand-name {
    position: absolute; inset: 0; display: flex; align-items: center; justify-content: center;
    text-align: center; font-family: var(--script); font-size: 26px; line-height: 1.05;
    color: var(--brand-blue);
  }
  .ingredients {
    position: absolute; left: 24px; top: 467px; width: 196px; height: 192px;
    background: var(--panel-pale); border-radius: 26px;
    font-family: var(--script); color: var(--ink); text-align: center;
    font-size: 17px; line-height: 23px; padding-top: 9px;
  }
  .ingredients h2 { font-weight: 400; font-size: 17px; text-decoration: underline; }
  .allergen {
    position: absolute; left: 0; width: 100%; top: 664px; text-align: center;
    font-family: var(--thin); font-size: 18px; color: var(--ink);
  }
  .batch {
    position: absolute; left: 9px; top: 690px;
    font-family: var(--thin); font-size: 26px; color: var(--ink);
  }
  .story {
    left: 10px; top: 24px; width: 226px;
    font-family: var(--script); font-size: 16.5px; line-height: 29px;
    color: var(--ink); text-align: center;
  }
  .recycle-title {
    position: absolute; left: 14px; top: 498px;
    font-family: var(--script); font-size: 24px; font-weight: 400;
    color: var(--ink); text-decoration: underline;
  }
  .recycle-steps {
    position: absolute; right: 18px; top: 540px; text-align: right;
    font-family: var(--script); font-size: 19px; line-height: 29px; color: var(--ink);
  }
  .bottles {
    position: absolute; left: 12px; top: 617px; width: 100px; height: 100px;
    border-radius: 10px;
    background: radial-gradient(ellipse at center, rgba(235,245,250,0.85) 0%, rgba(220,235,240,0.4) 60%, rgba(220,235,240,0) 80%);
  }
</style>
</head>
<body>
<main class="sheet">

  <section class="label label--back" aria-label="Back label">
    <div class="scenery" role="img" aria-label="Beach scene with sand, turquoise sea and cloudy blue sky"></div>
    <p class="flipped flavour">Lemonade</p>
    <div class="flipped brand">
      <svg viewBox="0 0 140 140" aria-hidden="true">
        <circle cx="70" cy="70" r="66" fill="rgba(255,255,255,0.55)" stroke="var(--ring)" stroke-width="3"/>
      </svg>
      <p class="brand-name">Marrowby<br>Cove Soda</p>
    </div>
    <div class="hole" aria-hidden="true"></div>
    <div class="ingredients">
      <h2>Ingredient</h2>
      <p>Purified Carbonated water</p>
      <p>Sugar</p>
      <p>Acidity Regulator (330, 331)</p>
      <p>Preservative (211)</p>
      <p>Stabilizers (414, 415)</p>
      <p>Permitted food colours</p>
      <p>Natural Flavours</p>
    </div>
    <p class="allergen">May contain Nuts etc.</p>
    <p class="batch">Batch ______________</p>
  </section>

  <section class="label label--reverse" aria-label="Reverse label">
    <div class="scenery" role="img" aria-label="Golden sand, sea horizon and deep blue sky with clouds"></div>
    <p class="flipped story">Designed and patented<br>for carbonated drinks in 1872<br>by British swig maker<br>Silas Pembrook of Ashgrove,<br>London, the glass bottle is<br>specially made to encase a round<br>marble and a rubber<br>washer in the neck.</p>
    <div class="hole" aria-hidden="true"></div>
    <h2 class="recycle-title">How to Recycle :-</h2>
    <p class="recycle-steps">The goli soda bottles<br>would go back<br>to get refilled<br>at a<br>factory.</p>
    <div class="bottles" role="img" aria-label="Three clear glass marble-stopper soda bottles on the sand"></div>
  </section>

</main>
</body>
</html>
```